Bright Harbor Real Estate Institute

This must be done in word press and I will need about 7 tabs The home page, Information page, Schedule and Cost page which will link to a Email me form, a online registration a about us and location/contact tab Each tab will then open several other pages. The home page will describe different courses that we offer since all the schools are about the same you can get a good ideal by going to qelvanto.org or pinnaclebayrealtyschool.com and looking at their site I would like mine to be similar as the courses are exactly the same but I would like the site to be more modern I also need it to be in word press so I can change it and update the dates as they change I have attached he logo below

Target Market(s)

people interested in getting into real estate and those who need continuing education

Coding

Coded - Design and coding required

Number of Pages Required

5+ page

Font styles to use
Sans Serif

Colors
3276b5

Requirements
Must have
• A page to schedule classes, a tab so the college I am partnering with can link the online courses to the back side, a page that describes the type of classes I offer

```html
<!DOCTYPE html>
<html lang="en">
<head>
<meta charset="utf-8">
<title>Bright Harbor Real Estate Institute</title>
<link href="https://fonts.googleapis.com/css2?family=Noto+Serif:wght@400;700&family=Open+Sans:wght@400;600&display=swap" rel="stylesheet">
<style>
:root{
  --brand:#3276b5;
  --charcoal:#424347;
  --panel:#ededed;
  --field:#c4c4c6;
  --ink:#555;
  --white:#fff;
}
*{box-sizing:border-box;margin:0;padding:0}
html,body{width:962px;height:1200px;overflow:hidden;background:var(--white)}
body{position:relative;font-family:"Noto Serif",serif;color:var(--ink)}
.abs{position:absolute}
.site-header{left:0;top:0;width:962px;height:77px;background:var(--white)}
.brand-name{left:164px;top:24px;width:200px;font-weight:700;font-size:15px;line-height:17px;color:var(--brand)}
.brand-mark{left:150px;top:28px;width:10px;height:10px;background:var(--brand)}
.contact-item{font-family:"Open Sans",sans-serif;font-size:8px;line-height:11px;color:#333}
.contact-item strong{color:var(--brand);font-weight:600;font-size:9px}
.main-nav{left:0;top:77px;width:962px;height:38px;background:var(--brand);display:flex;align-items:center;padding-left:183px;gap:32px}
.main-nav a{font-family:"Open Sans",sans-serif;font-size:11px;color:#dbe8f5;text-decoration:none;letter-spacing:.2px}
.hero{left:0;top:115px;width:962px;height:349px;background:#f4f6f8;overflow:hidden}
.hero-visual{left:350px;top:0;width:612px;height:349px;background:linear-gradient(100deg,#f4f6f8 0%,#dfe8f0 30%,#c9d6e3 60%,#8ea6c0 80%,#e8eef4 100%)}
.hero-title{left:153px;top:117px;font-size:17px;color:#333;white-space:nowrap}
.hero-title b{color:var(--brand);font-weight:700}
.btn{height:39px;width:118px;border:1px solid;border-radius:2px;font-size:12px;display:flex;align-items:center;justify-content:center;background:transparent}
.btn-outline-blue{left:199px;top:174px;border-color:var(--brand);color:var(--brand)}
.btn-outline-dark{left:334px;top:174px;border-color:#333;color:#333}
.content-field{left:0;top:464px;width:962px;height:619px;background:var(--field)}
.card{background:var(--panel)}
.card p{font-size:10.5px;line-height:13.5px;color:var(--ink);margin-bottom:8px}
.card p a{color:var(--brand)}
.card-foot{position:absolute;left:0;bottom:0;width:100%;color:var(--white);text-align:center}
.card-foot h3{font-weight:400;font-size:17px;letter-spacing:2px}
.card-foot a{font-family:"Open Sans",sans-serif;font-size:8.5px;color:var(--white);display:block;margin-top:6px}
.foot-blue{background:var(--brand)}
.foot-dark{background:var(--charcoal)}
.feature-head{position:absolute;left:0;top:0;width:100%;height:39px;background:var(--charcoal);color:var(--white);display:flex;align-items:center;justify-content:space-between;padding:0 15px}
.feature-head h3{font-weight:400;font-size:17px;letter-spacing:1px}
.feature-head a{font-size:9px;color:var(--white)}
.feature-text{position:absolute;font-size:10.5px;line-height:13.7px;color:var(--ink)}
.help-title{left:201px;top:992px;font-size:33px;color:var(--brand);white-space:nowrap}
.help-note{left:585px;top:990px;font-size:8.5px;line-height:11px;color:var(--brand)}
.help-number{left:585px;top:1016px;font-size:18px;font-weight:700;color:var(--brand);letter-spacing:.5px}
.site-footer{left:0;top:1083px;width:962px;height:117px;text-align:center;padding-top:26px;font-size:11px;color:#666}
</style>
</head>
<body>
<header class="site-header abs">
  <div class="brand-mark abs"></div>
  <div class="brand-name abs">Bright Harbor Real Estate Institute</div>
  <svg class="abs" style="left:516px;top:26px" width="20" height="28" viewBox="0 0 20 28"><path d="M10 0C4.5 0 0 4.4 0 9.8 0 17 10 28 10 28s10-11 10-18.2C20 4.4 15.5 0 10 0z" fill="#3276b5"/><circle cx="10" cy="10" r="4" fill="#fff"/></svg>
  <div class="contact-item abs" style="left:557px;top:23px">0123 Your address,<br>here 000<br><strong>Town, AA 0000</strong></div>
  <svg class="abs" style="left:666px;top:25px" width="22" height="28" viewBox="0 0 24 24"><path d="M6.6 10.8c1.4 2.8 3.8 5.1 6.6 6.6l2.2-2.2c.3-.3.7-.4 1-.2 1.1.4 2.3.6 3.6.6.6 0 1 .4 1 1V20c0 .6-.4 1-1 1C10.6 21 3 13.4 3 4c0-.6.4-1 1-1h3.5c.6 0 1 .4 1 1 0 1.3.2 2.5.6 3.6.1.3 0 .7-.2 1L6.6 10.8z" fill="#3276b5"/></svg>
  <div class="contact-item abs" style="left:705px;top:27px">TOLLFREE<br><strong>555-555-555</strong></div>
</header>

<nav class="main-nav abs">
  <a>HOME</a><a>INFORMATION</a><a>SCHEDULE AND COST</a><a>ONLINE REGISTRATION</a><a>ABOUT US</a><a>CONTACT</a>
</nav>

<section class="hero abs">
  <div class="hero-visual abs" role="img" aria-label="Photo of a young student looking at a cut-away model house surrounded by playful sketches"></div>
  <h1 class="hero-title abs" style="font-weight:400">Welcome to <b>Bright Harbor</b> Real Estate Institute</h1>
  <div class="btn btn-outline-blue abs">LREARN MORE</div>
  <div class="btn btn-outline-dark abs">REGISTER</div>
</section>

<main class="content-field abs">
  <div class="card abs" style="left:150px;top:38px;width:181px;height:215px">
    <div style="padding:15px 8px 0 16px">
      <p>The Bright Harbor Real Estate Institute requires 90 hours of training and subsequent testing to become licensed.</p>
      <p>The training for the initial licensing consists of two mandatory courses.</p>
    </div>
    <div class="card-foot foot-blue" style="height:81px;padding-top:18px"><h3>Information</h3><a>LEARN MORE</a></div>
  </div>

  <div class="card abs" style="left:353px;top:38px;width:245px;height:215px">
    <svg class="abs" style="left:73px;top:22px" width="100" height="98" viewBox="0 0 100 98">
      <g fill="none" stroke="#3276b5" stroke-width="6">
        <rect x="3" y="10" width="80" height="72" rx="4"/>
        <line x1="3" y1="28" x2="83" y2="28"/>
        <line x1="18" y1="0" x2="18" y2="18"/><line x1="66" y1="0" x2="66" y2="18"/>
        <line x1="28" y1="10" x2="56" y2="10"/>
      </g>
      <g fill="#3276b5"><rect x="14" y="40" width="14" height="10"/><rect x="34" y="40" width="14" height="10"/><rect x="54" y="40" width="14" height="10"/><rect x="14" y="58" width="14" height="10"/><rect x="34" y="58" width="14" height="10"/></g>
      <circle cx="72" cy="72" r="24" fill="#ededed" stroke="#3276b5" stroke-width="6"/>
      <path d="M60 70l9 10 24-26" fill="none" stroke="#3276b5" stroke-width="7"/>
    </svg>
    <div class="card-foot foot-dark" style="height:81px;padding-top:22px"><h3>Schedule &amp; Cost</h3><a>LEARN MORE</a></div>
  </div>

  <div class="card abs" style="left:620px;top:38px;width:180px;height:217px">
    <div style="padding:11px 8px 0 12px">
      <p><a>Sign up</a> today and start in your real estate career. Our online registration is secured by Veridane SSL Certification.</p>
      <p>We do not require pre-deposit or charge different prices at the door.</p>
    </div>
    <div class="card-foot foot-blue" style="height:81px;padding-top:18px"><h3>Registration</h3><a>LEARN MORE</a></div>
  </div>

  <div class="card abs" style="left:151px;top:291px;width:313px;height:195px">
    <div class="feature-head"><h3>Online Courses</h3><a>LEARN MORE</a></div>
    <svg class="abs" style="left:25px;top:70px" width="82" height="82" viewBox="0 0 82 82">
      <g fill="none" stroke="#3276b5" stroke-width="4">
        <circle cx="41" cy="41" r="38"/><ellipse cx="41" cy="41" rx="17" ry="38"/>
        <line x1="41" y1="3" x2="41" y2="79"/><line x1="3" y1="41" x2="79" y2="41"/>
        <path d="M9 22h64M9 60h64"/>
      </g>
    </svg>
    <div class="feature-text" style="left:130px;top:68px;width:165px">Bright Harbor Real Estate Institute offers two online courses for students to complete their 90 hours to qualify for licensing and be eligible for the licensing exam.</div>
  </div>

  <div class="card abs" style="left:487px;top:292px;width:313px;height:195px">
    <div class="feature-head"><h3>Why Bright Harbor?</h3><a>LEARN MORE</a></div>
    <svg class="abs" style="left:27px;top:72px" width="82" height="82" viewBox="0 0 82 82">
      <circle cx="41" cy="41" r="41" fill="#3276b5"/>
      <path d="M28 30c0-8 6-13 14-13s13 5 13 12c0 9-10 10-10 19v3" fill="none" stroke="#ededed" stroke-width="9"/>
      <circle cx="41" cy="64" r="6" fill="#ededed"/>
    </svg>
    <div class="feature-text" style="left:132px;top:66px;width:165px">We have been locally owned and operated since the mid 1970’s and are accredited by Lakemont Real Estate Commission.</div>
  </div>

  <svg class="abs" style="left:515px;top:524px" width="55" height="55" viewBox="0 0 55 55">
    <circle cx="27.5" cy="27.5" r="25" fill="none" stroke="#3276b5" stroke-width="3"/>
    <path d="M20 15c2 0 4 4 4 6s-3 2-3 4c1 4 4 7 8 9 2 0 2-3 4-3s6 2 6 4c0 3-3 5-6 5-9-1-18-10-19-19 0-3 3-6 6-6z" fill="#3276b5"/>
  </svg>
</main>

<div class="help-title abs">Need Some Help?</div>
<div class="help-note abs">Our support team would love to help you.<br>don’t hesitate and give Us a call</div>
<div class="help-number abs">1.555.555.5</div>

<footer class="site-footer abs">© Copyrights Bright Harbor Real Estate Institute</footer>
</body>
</html>
```